" A Quitavel é uma empresa que desenvolve e fornece o sistema de cobrança Quitavel para empresas de cobrança (escritórios de cobrança, assessorias de cobranças, escritórios de advogados), tais clientes chamamos de ASSESSORIAS, e também fornecemos o sistema para empresas que possuem uma grande quantidade de clientes inadimplentes e que fazem a cobrança destes clientes internamente através de um departamento de cobrança, estes clientes chamamos de CREDORES. Alguns clientes ASSESSORIAS: www.grupoltn-exemplo.com.br www.moraisetavares-exemplo.com.br www.rvrecupera-exemplo.com.br Alguns clientes CREDORES: www.linguaviva-exemplo.com www.grupovelarium-exemplo.com.br www.ronaldos-exemplo.com.br Todos os produtos e serviços que comercializamos são através da plataforma Quitavel, por exemplo, para que um cliente utilize nosso produto “Portal de Negociação” ele precisa contratar o Quitavel já que suas configurações são através do sistema, da mesma forma o serviço de “SMS”, já que as campanhas são criadas e disparadas pelo sistema Quitavel. O sistema Quitavel “nasceu” primeiro que a empresa Quitavel, já que dois dos atuais sócios possuíram uma empresa anterior de 2012 até a abertura da Quitavel em 1 de setembro de 2015. Esta empresa desenvolvia um sistema focado para assessorias de cobrança, porém em uma tecnologia antiga, e então resolveram criar um novo software com tecnologias atuais na época e para isto buscaram um investidor e juntos optaram por criar uma nova empresa, uma nova marca. Nossa logo foi construída através da plataforma Marca Pronta e gostamos muito do resultado! E estamos aqui novamente buscando que seus profissionais nos ajudem a criar novos materiais que hoje se fazem necessários para nós. "

```html
<!DOCTYPE html>
<html lang="pt-BR">
<head>
<meta charset="UTF-8">
<title>Quitavel — Como Funciona?</title>
<link rel="stylesheet" href="https://fonts.googleapis.com/css2?family=Open+Sans:wght@400;600;700&display=swap">
<style>
  :root{
    --page-bg:#eceef1;
    --slide-bg:#ffffff;
    --band-blue:#1f3f8f;
    --panel-navy:#17264a;
    --title-blue:#1f4e8c;
    --frame-grey:#b9bcc2;
    --text-grey:#555a62;
    --arrow-grey:#4a4c50;
    --platform-grey:#4a4c50;
    --product-navy:#0f2a5c;
    --partner-green:#2f8a3c;
    --service-orange:#d9731c;
    --white:#ffffff;
  }
  *{box-sizing:border-box;margin:0;padding:0}
  html,body{width:1200px;height:1200px;overflow:hidden}
  body{background:var(--page-bg);font-family:"Open Sans",Arial,sans-serif;position:relative}
  .slide{position:absolute;left:0;top:262px;width:1200px;height:675px;background:var(--slide-bg);overflow:hidden}
  .side-band{position:absolute;left:0;top:0;width:20px;height:100%;background:var(--band-blue)}
  .brand-panel{position:absolute;left:954px;top:0;width:246px;height:100%;
    background:linear-gradient(160deg,#1d2e56 0%,var(--panel-navy) 60%,#121e3b 100%);color:var(--white)}
  .brand-name{position:absolute;left:0;right:0;top:140px;text-align:center;font-size:32px;font-weight:600;color:var(--white)}
  .brand-copy{position:absolute;left:34px;right:24px;top:225px;font-size:17px;line-height:1.7}
  .brand-copy strong{font-weight:700}

  .slide-title{position:absolute;left:125px;top:30px;font-size:27px;font-weight:700;color:var(--title-blue)}
  .title-rule{position:absolute;left:120px;top:76px;width:830px;height:2px;background:var(--title-blue)}

  .diagram-frame{position:absolute;left:117px;top:86px;width:782px;height:553px;border:2px solid var(--frame-grey);border-radius:16px}
  .col-head{position:absolute;top:104px;font-size:16px;font-weight:700;color:var(--text-grey);transform:translateX(-50%)}
  .col-rail{position:absolute;border:2px solid var(--frame-grey);border-radius:14px;background:var(--white)}
  .box{position:absolute;display:flex;align-items:center;justify-content:center;text-align:center;
    border-radius:10px;font-size:12.5px;line-height:1.2;padding:0 3px}
  .box--company{left:145px;width:92px;height:60px;border:2px solid var(--frame-grey);color:var(--text-grey);background:var(--white)}
  .box--platform{left:287px;width:76px;height:44px;background:var(--platform-grey);color:var(--white)}
  .box--product{left:421px;width:76px;height:58px;background:var(--product-navy);color:var(--white)}
  .box--partner{left:553px;width:84px;height:58px;background:var(--partner-green);color:var(--white);font-size:11.5px}
  .box--service{left:692px;width:88px;height:40px;background:var(--service-orange);color:var(--white);font-size:12px}
  .box--service-small{font-size:10px;padding:0 2px}
  .arrows{position:absolute;left:0;top:0}
</style>
</head>
<body>
<section class="slide">
  <div class="side-band"></div>

  <h1 class="slide-title">Como Funciona?</h1>
  <div class="title-rule"></div>

  <div class="diagram-frame"></div>

  <span class="col-head" style="left:200px">Empresas</span>
  <span class="col-head" style="left:326px">Plataforma</span>
  <span class="col-head" style="left:459px">Produtos</span>
  <span class="col-head" style="left:595px">Parceiros</span>
  <span class="col-head" style="left:736px">Serviços</span>

  <div class="col-rail" style="left:273px;top:145px;width:104px;height:476px"></div>
  <div class="col-rail" style="left:405px;top:145px;width:108px;height:476px"></div>
  <div class="col-rail" style="left:541px;top:145px;width:108px;height:476px"></div>
  <div class="col-rail" style="left:675px;top:145px;width:122px;height:476px"></div>

  <div class="box box--company" style="top:146px">Assessorias de cobrança</div>
  <div class="box box--company" style="top:230px">Escritórios jurídicos</div>
  <div class="box box--company" style="top:308px">Instituições financeiras</div>
  <div class="box box--company" style="top:391px">Varejo</div>
  <div class="box box--company" style="top:475px">Educação</div>
  <div class="box box--company" style="top:550px">Serviços</div>

  <div class="box box--platform" style="top:318px">Web</div>
  <div class="box box--platform" style="top:399px">API</div>

  <div class="box box--product" style="top:231px">CRM de cobrança</div>
  <div class="box box--product" style="top:309px">Discador automático</div>
  <div class="box box--product" style="top:390px">Portal de negociação</div>
  <div class="box box--product" style="top:468px">Canais de negociação</div>

  <div class="box box--partner" style="top:231px">Infraestrutura</div>
  <div class="box box--partner" style="top:309px">Telecom</div>
  <div class="box box--partner" style="top:390px">Mensageria</div>
  <div class="box box--partner" style="top:471px">Informações cadastrais</div>

  <div class="box box--service box--service-small" style="top:152px">Desenvolvimento de integrações</div>
  <div class="box box--service" style="top:204px">Implantação</div>
  <div class="box box--service" style="top:256px">Suporte contínuo</div>
  <div class="box box--service" style="top:308px">SMS</div>
  <div class="box box--service" style="top:360px">E-mail</div>
  <div class="box box--service" style="top:412px">Vozbot</div>
  <div class="box box--service" style="top:464px">Conversa Já</div>
  <div class="box box--service" style="top:516px">Chat Social</div>
  <div class="box box--service" style="top:568px">Torpedo de voz</div>

  <svg class="arrows" width="954" height="675" viewBox="0 0 954 675" aria-hidden="true">
    <g stroke="#4a4c50" stroke-width="2.5" fill="none">
      <line x1="248" y1="176" x2="262" y2="176"/>
      <line x1="248" y1="260" x2="262" y2="260"/>
      <line x1="248" y1="338" x2="262" y2="338"/>
      <line x1="248" y1="421" x2="262" y2="421"/>
      <line x1="248" y1="505" x2="262" y2="505"/>
      <line x1="248" y1="580" x2="262" y2="580"/>
      <line x1="386" y1="380" x2="396" y2="380"/>
      <line x1="522" y1="380" x2="532" y2="380"/>
      <line x1="657" y1="380" x2="667" y2="380"/>
    </g>
    <g fill="#4a4c50">
      <path d="M243,176 l7,-5 v10z M267,176 l-7,-5 v10z"/>
      <path d="M243,260 l7,-5 v10z M267,260 l-7,-5 v10z"/>
      <path d="M243,338 l7,-5 v10z M267,338 l-7,-5 v10z"/>
      <path d="M243,421 l7,-5 v10z M267,421 l-7,-5 v10z"/>
      <path d="M243,505 l7,-5 v10z M267,505 l-7,-5 v10z"/>
      <path d="M243,580 l7,-5 v10z M267,580 l-7,-5 v10z"/>
      <path d="M381,380 l6,-4 v8z M401,380 l-6,-4 v8z"/>
      <path d="M517,380 l6,-4 v8z M537,380 l-6,-4 v8z"/>
      <path d="M652,380 l6,-4 v8z M672,380 l-6,-4 v8z"/>
    </g>
  </svg>

  <aside class="brand-panel">
    <div class="brand-name">Quitavel</div>
    <p class="brand-copy">Reunimos na plataforma toda a experiência dos nossos profissionais de negócios, tecnologia e design empenhados em só objetivo: <strong>Construir o melhor sistema de cobrança do mercado</strong></p>
  </aside>
</section>
</body>
</html>
```